Real Estate Sign 2

Our company is called Harwick Tolland Realty. We are a real estate development company. We need a sign that we are going to hang outside of our projects that says: Another project brought to you by Harwick Tolland Realty... For Sale....(213) 555-0847. At the very bottom is needs to say CaBRE# 04736291" We want the Harwick Tolland Realty to be sophisticated, fresh, simple. We do not have a logo so maybe one can be incorporated into the sign. Sign will be about 30"x24"

Industry/Entity Type

Real Estate

```html
<!DOCTYPE html>
<html lang="en">
<head>
<meta charset="UTF-8">
<title>Harwick Tolland Realty – For Sale Sign</title>
<link href="https://fonts.googleapis.com/css2?family=Anton&display=swap" rel="stylesheet">
<style>
  :root {
    --orange: #ff7a10;
    --orange-deep: #f25a00;
    --red-edge: #e8321a;
    --navy: #141a6e;
    --grey-panel: #ebebeb;
    --ink: #000000;
    --paper: #ffffff;
  }
  html, body {
    margin: 0;
    padding: 0;
    overflow: hidden;
    background: var(--paper);
  }
  .sign {
    position: relative;
    width: 1200px;
    height: 960px;
    overflow: hidden;
    background: var(--paper);
    font-family: "Anton", "Impact", sans-serif;
  }
  .sign__bands {
    position: absolute;
    inset: 0;
  }
  .tagline-panel {
    position: absolute;
    left: 0;
    top: 202px;
    width: 626px;
    height: 190px;
    background: var(--grey-panel);
    display: flex;
    flex-direction: column;
    justify-content: center;
    padding-left: 42px;
    box-sizing: border-box;
  }
  .tagline {
    margin: 0;
    color: var(--ink);
    font-size: 74px;
    line-height: 88px;
    letter-spacing: 0.01em;
  }
  .brand-panel {
    position: absolute;
    left: 626px;
    top: 200px;
    width: 540px;
    height: 194px;
    background: var(--navy);
    display: flex;
    align-items: center;
    justify-content: center;
  }
  .brand-name {
    margin: 0;
    color: var(--orange);
    font-size: 60px;
    line-height: 1.1;
    text-align: center;
    letter-spacing: 0.02em;
  }
  .headline {
    position: absolute;
    left: 0;
    width: 1200px;
    top: 400px;
    margin: 0;
    text-align: center;
    color: var(--ink);
    font-size: 205px;
    line-height: 220px;
    letter-spacing: 0.12em;
    text-indent: 0.12em;
  }
  .phone {
    position: absolute;
    left: 0;
    width: 1200px;
    top: 722px;
    margin: 0;
    text-align: center;
    color: var(--paper);
    font-size: 150px;
    line-height: 170px;
    letter-spacing: 0.03em;
    text-shadow: 2px 4px 6px rgba(0, 0, 0, 0.45);
  }
  .license {
    position: absolute;
    left: 0;
    width: 1200px;
    top: 884px;
    margin: 0;
    text-align: center;
    color: var(--orange);
    font-size: 46px;
    line-height: 60px;
    letter-spacing: 0.02em;
  }
</style>
</head>
<body>
<main class="sign">
  <svg class="sign__bands" width="1200" height="960" viewBox="0 0 1200 960" aria-hidden="true">
    <defs>
      <linearGradient id="orangeBand" x1="0" y1="0" x2="0" y2="1">
        <stop offset="0" stop-color="var(--orange)" style="stop-color:#ff8a1c"/>
        <stop offset="1" stop-color="var(--orange-deep)" style="stop-color:#f25a00"/>
      </linearGradient>
    </defs>
    <polygon class="band band--top" points="0,0 1200,0 1200,20 0,96" fill="url(#orangeBand)"/>
    <line class="band-edge" x1="0" y1="96" x2="1200" y2="20" stroke="#e8321a" stroke-width="2"/>
    <polygon class="band band--bottom" points="0,694 1200,616 1200,712 0,712" fill="url(#orangeBand)"/>
    <rect class="band band--navy" x="0" y="710" width="1200" height="250" fill="#141a6e"/>
  </svg>

  <section class="tagline-panel">
    <p class="tagline">Another project<br>brought to you by</p>
  </section>

  <section class="brand-panel">
    <p class="brand-name">Harwick Tolland<br>Realty</p>
  </section>

  <h1 class="headline">FOR SALE</h1>

  <p class="phone">(213) 555-0847</p>
  <p class="license">CaBRE# 04736291</p>
</main>
</body>
</html>
```